Will you marry me post card

I am just looking for a postcard to send my partner that will ask him to marry me.
I plan on creating about 200 of them and mailing them all at once so that he gets them all on the same day.
They should all be similar or could have a few different options.
I would like it simple, elegant, clean and crisp. No images, just text or icons

My only requirement is the text, "will you marry me?" in all lowercase -- any fonts, can be big, small, varying sizes, repeated, whole card, tiny space, don't care...just amazing design. BUT SIMPLE!

```html
<!DOCTYPE html>
<html lang="en">
<head>
<meta charset="utf-8">
<title>will you marry me? — postcard</title>
<link rel="stylesheet" href="https://fonts.googleapis.com/css2?family=Questrial&family=Montserrat:wght@400;500&family=Archivo+Narrow:wght@400&display=swap">
<style>
  :root {
    --backdrop: #e8ebeb;
    --card: #ffffff;
    --ink: #161616;
    --sage: #8e9b98;
    --card-shadow: rgba(40, 50, 50, 0.18);
  }
  html, body {
    margin: 0;
    padding: 0;
    width: 1200px;
    height: 1000px;
    overflow: hidden;
    background: var(--backdrop);
  }
  .postcard {
    position: absolute;
    left: 100px;
    top: 180px;
    width: 1000px;
    height: 640px;
    background: var(--card);
    box-shadow: 0 12px 40px var(--card-shadow);
    overflow: hidden;
  }
  .phrase {
    position: absolute;
    margin: 0;
    white-space: nowrap;
    font-weight: 400;
  }
  .phrase span { vertical-align: baseline; }

  /* headline across the middle */
  .phrase--main {
    right: 120px;
    top: 228px;
    font-family: "Questrial", sans-serif;
    color: var(--ink);
    font-size: 66px;
    line-height: 110px;
    letter-spacing: 1px;
  }
  .phrase--main .w-will { font-size: 44px; }
  .phrase--main .w-you { font-size: 104px; letter-spacing: 2px; }

  /* small echoes in sage */
  .phrase--echo {
    font-family: "Montserrat", sans-serif;
    color: var(--sage);
    font-weight: 500;
    font-size: 28px;
    line-height: 50px;
  }
  .phrase--echo .w-will { font-size: 22px; }
  .phrase--echo .w-you { font-size: 34px; }
  .phrase--echo .w-me { font-size: 42px; }
  .phrase--echo-upper { right: 120px; top: 168px; }
  .phrase--echo-lower { left: 160px; top: 336px; }

  /* vertical phrase along the left edge */
  .phrase--edge-left {
    left: 28px;
    top: 600px;
    transform: rotate(-90deg);
    transform-origin: 0 0;
    font-family: "Montserrat", sans-serif;
    color: var(--sage);
    font-weight: 500;
    font-size: 44px;
    line-height: 72px;
  }
  .phrase--edge-left .w-will { font-size: 34px; }
  .phrase--edge-left .w-you { font-size: 60px; }
  .phrase--edge-left .w-me { font-size: 54px; }

  /* condensed vertical phrase on the right */
  .phrase--edge-right {
    left: 872px;
    top: 612px;
    transform: rotate(-90deg);
    transform-origin: 0 0;
    font-family: "Archivo Narrow", sans-serif;
    color: var(--sage);
    font-size: 30px;
    line-height: 44px;
  }
  .phrase--edge-right .w-will { font-size: 22px; }
  .phrase--edge-right .w-you { font-size: 40px; }
  .phrase--edge-right .w-me { font-size: 34px; }
</style>
</head>
<body>
  <main class="postcard">
    <p class="phrase phrase--edge-left"><span class="w-will">will</span> <span class="w-you">you</span> <span class="w-marry">marry</span> <span class="w-me">me?</span></p>

    <p class="phrase phrase--echo phrase--echo-upper"><span class="w-will">will</span> <span class="w-you">you</span> <span class="w-marry">marry</span> <span class="w-me">me</span>?</p>

    <h1 class="phrase phrase--main"><span class="w-will">will</span> <span class="w-you">you</span> marry me?</h1>

    <p class="phrase phrase--echo phrase--echo-lower"><span class="w-will">will</span> <span class="w-you">you</span> <span class="w-marry">marry</span> <span class="w-me">me</span>?</p>

    <p class="phrase phrase--edge-right"><span class="w-will">will</span> <span class="w-you">you</span> <span class="w-marry">marry</span> <span class="w-me">me?</span></p>
  </main>
</body>
</html>
```